Basic Web Design and coding (wordpress ideally). Needed live by 10th Feb!

Hi,

We are a Financial Wellness company that provides free seminars to help educate the general public and guide them to becoming debt free and prosperous.

Our company provides insurance, mortgage/ home loan and investment advice.

We require a fairly basic website that shouldn't require more then just a few pages.

The key elements to the site are as follows;

1: clean and easy to use (both on the front and back end). Clean calls to action and easy to use.

2: 4 "buttons" on the home page for the customer to choose which service they require from us which leads to a data capture form.

3: A (live?) calendar that shows all the seminars we provide across the country (location, date, time, etc) and also allows customers to register their attendance via the website. No payment is taken, just data capture. - this doesn't have to be live as long as it can be updated as needed.

4: Google analytic

5: Responsive (phone, tablet etc)

Other than that its just Home, About Us, Services, Contact etc.

We already have the logo and color scheme (blue, green, white and black).

Here are a couple of templates that we like the design of - please note the position of the 4 "tabs/buttons" as these need to be seen on the home screen.

1) http://www.pagecrafthub.example/demo/52036.html

2) http://www.pagecrafthub.example/demo/45686.html

I will be choosing a design/contractor before the job closes.

Thank you.

Education

5+ page

• Coding. Brand continuity (color scheme), 4 buttons on the home screen, calendar.

```html
<!DOCTYPE html>
<html lang="en">
<head>
<meta charset="utf-8">
<title>Northvale Wellness Group – Home</title>
<link href="https://fonts.googleapis.com/css2?family=Open+Sans:wght@400;600;700&display=swap" rel="stylesheet">
<style>
:root{
  --blue:#2b55a3;
  --blue-dark:#24498f;
  --green:#35a57a;
  --grey-bg:#f3f3f3;
  --text:#555;
  --muted:#b5b5b5;
  --line:#e1e1e1;
  --white:#fff;
}
*{box-sizing:border-box;margin:0;padding:0}
html,body{width:1200px;height:2378px;overflow:hidden}
body{position:relative;font-family:'Open Sans',Arial,sans-serif;color:var(--text);background:var(--white)}
.abs{position:absolute}

/* header */
.topline{left:0;top:0;width:1200px;height:4px;background:var(--green)}
.header{left:0;top:4px;width:1200px;height:78px;background:var(--white);box-shadow:0 2px 4px rgba(0,0,0,.08);z-index:3}
.brand{left:98px;top:-30px;width:216px;height:216px;border-radius:50%;background:var(--white);z-index:4;display:flex;align-items:center;justify-content:center;text-align:center;box-shadow:0 3px 6px rgba(0,0,0,.15);padding-top:30px}
.brand span{color:var(--blue);font-weight:700;font-size:22px;line-height:1.2;letter-spacing:1px}
.nav{left:440px;top:34px;display:flex;gap:0;z-index:4}
.nav a{position:absolute;font-size:14px;font-weight:600;color:#333;text-decoration:none;white-space:nowrap}
.nav a.active{color:var(--green)}
.nav a.active::after{content:"";position:absolute;left:8px;right:8px;top:24px;height:3px;border-radius:3px;background:var(--green)}
.phone{left:952px;top:26px;display:flex;align-items:center;gap:14px;z-index:4}
.phone svg{width:30px;height:30px}
.phone small{display:block;font-size:12px;color:#444}
.phone b{display:block;font-size:16px;color:#333;font-weight:700}

/* hero */
.hero{left:0;top:82px;width:1200px;height:538px;background:linear-gradient(100deg,#d8d2ca 0%,#b9b0a6 40%,#8c8178 70%,#4b4a55 100%)}
.hero-title{left:98px;top:286px;color:var(--white);font-size:33px;line-height:1.3;font-weight:600}
.hero-title b{font-weight:700}
.hero-arrow{top:328px;width:44px;height:44px;border-radius:50%;border:2px solid rgba(255,255,255,.85);background:rgba(0,0,0,.35);display:flex;align-items:center;justify-content:center}

/* services */
.help{left:0;top:620px;width:1200px;height:466px;background:var(--grey-bg)}
.section-title{left:0;width:1200px;text-align:center;font-size:25px;font-weight:700;color:var(--blue)}
.section-title em{font-style:normal;color:var(--green)}
.section-title small{font-size:15px;font-weight:600;color:#333}
.card{top:777px;width:235px;height:244px;color:var(--white);text-align:center;padding-top:96px;box-shadow:0 14px 14px -10px rgba(0,0,0,.2)}
.card.blue{background:var(--blue)}
.card.green{background:var(--green)}
.card .icon{position:absolute;left:52px;top:-57px;width:130px;height:130px;border-radius:50%;background:var(--white);border:3px solid;display:flex;align-items:center;justify-content:center}
.card.blue .icon{border-color:var(--blue)}
.card.green .icon{border-color:var(--green)}
.card h3{font-size:17px;font-weight:600;letter-spacing:.5px}
.card hr{width:56px;border:0;border-top:2px solid var(--white);margin:12px auto 14px}
.card p{font-size:12.5px;line-height:1.65;padding:0 22px}

/* calendar */
.next{left:98px;top:1182px;width:251px;height:305px;background:var(--blue);color:var(--white);text-align:center}
.next .day{position:absolute;left:0;width:251px;top:24px;font-weight:700;font-size:16px}
.next .chev{position:absolute;left:22px;top:22px;font-size:18px}
.next .num{position:absolute;left:0;width:251px;top:92px;font-size:76px;font-weight:400}
.next .link{position:absolute;left:0;width:251px;top:258px;font-size:15px;font-weight:600}
.month{top:1182px;width:266px;height:305px;border:1px solid var(--line);border-left:0}
.month h4{position:absolute;left:0;width:100%;top:24px;text-align:center;font-size:16px;color:var(--blue);font-weight:700}
.month .arrow{position:absolute;right:28px;top:20px;font-size:18px;color:var(--blue)}
.grid{position:absolute;left:16px;top:68px;display:grid;grid-template-columns:repeat(7,34px);grid-auto-rows:31px;font-size:13px;text-align:center;align-items:center;justify-items:center}
.grid .h{font-weight:700;color:#444;font-size:12px}
.grid span{color:#444;width:26px;height:26px;line-height:26px}
.grid .o{color:var(--muted)}
.grid .c{border:1.5px solid #aaa;border-radius:50%;line-height:23px}
.grid .cb{border:2px solid var(--blue);border-radius:50%;line-height:22px}
.month .plus{position:absolute;right:24px;bottom:12px;width:26px;height:26px;border:2px solid var(--green);border-radius:50%;color:var(--green);text-align:center;line-height:20px;font-size:20px}
.allsem{left:883px;top:1182px;width:217px;height:305px;border:2px solid var(--green);padding:20px 18px}
.allsem h4{text-align:center;color:var(--green);font-size:15px;font-weight:700;margin-bottom:20px}
.allsem li{list-style:none;position:relative;padding-left:22px;font-size:12.5px;line-height:1.5;margin-bottom:9px;color:#555}
.allsem li::before{content:"";position:absolute;left:2px;top:3px;width:5px;height:9px;border:solid var(--green);border-width:0 2px 2px 0;transform:rotate(45deg)}

/* events */
.events{left:98px;width:1002px;height:241px;border:1px solid var(--line);box-shadow:0 1px 2px rgba(0,0,0,.06);display:flex;padding:32px 0}
.event{flex:1;padding:0 30px;border-right:1px solid var(--line)}
.event:last-child{border-right:0}
.event .date{font-size:11px;font-weight:700;color:var(--green)}
.event .time{font-size:13.5px;font-weight:700;color:var(--blue-dark);margin-top:2px}
.event p{font-size:13px;line-height:1.5;margin-top:12px;height:80px;color:#555}
.event .actions{display:flex;gap:6px;margin-top:16px}
.btn{font-size:11.5px;height:28px;padding:0 8px;display:flex;align-items:center;gap:4px}
.btn.loc{background:#eaeaea;color:#555}
.btn.reg{background:var(--green);color:var(--white);font-weight:600}

/* footer */
.footer{left:0;top:2080px;width:1200px;height:223px;background:linear-gradient(#2f5cab,#2a4f98);color:var(--white)}
.f-brand{left:98px;top:54px;width:170px;text-align:center;font-size:20px;font-weight:700;line-height:1.25;letter-spacing:1px}
.f-col{top:42px}
.f-col h5{font-size:17px;font-weight:400;margin-bottom:12px}
.f-col li{list-style:none;font-size:13px;line-height:25.5px;display:flex;align-items:center;gap:10px}
.f-col li::before{content:"";width:8px;height:8px;border:1.5px solid var(--white);border-radius:50%}
.f-news p{font-size:13px;margin-bottom:16px}
.f-news .input{width:206px;height:36px;background:var(--white);color:#777;font-size:12px;padding:10px 14px}
.f-news .sub{margin-top:12px;width:116px;height:38px;background:var(--green);font-weight:700;font-size:14px;display:flex;align-items:center;justify-content:center}
.bottom{left:0;top:2303px;width:1200px;height:75px;background:var(--green);color:var(--white)}
.bottom p{position:absolute;left:98px;top:28px;font-size:12px}
.social{position:absolute;left:916px;top:20px;display:flex;gap:6px}
.social span{width:32px;height:32px;border:1.5px solid var(--white);border-radius:50%}
</style>
</head>
<body>
<div class="abs topline"></div>
<header class="abs header"></header>
<div class="abs brand"><span>NORTHVALE<br>WELLNESS<br>GROUP</span></div>
<nav class="abs nav">
  <a class="active" style="left:20px">HOME</a>
  <a style="left:118px">ABOUT US</a>
  <a style="left:229px">SEMINARS</a>
  <a style="left:332px">SERVICE</a>
  <a style="left:433px">CONTACT</a>
</nav>
<div class="abs phone">
  <svg viewBox="0 0 30 30"><circle cx="15" cy="15" r="13.5" fill="none" stroke="#444" stroke-width="1.5"/><path d="M11 9c1 0 2 2 2 3s-1 1.5-1 2 2 4 4 4c.5 0 1-1 2-1s3 1 3 2-1.5 2-2.5 2C14 21 9 16 9 11c0-1 1-2 2-2z" fill="#444"/></svg>
  <div><small>Phone:</small><b>0400 317 264</b></div>
</div>

<section class="abs hero" role="img" aria-label="Photo of a smiling speaker in a suit holding a microphone before a seminar audience"></section>
<h1 class="abs hero-title">Prepopulates with<br>next Seminar based<br>on the <b>CALENDAR</b></h1>
<div class="abs hero-arrow" style="left:24px"><svg width="14" height="14" viewBox="0 0 14 14"><path d="M9 2 4 7l5 5" fill="none" stroke="#fff" stroke-width="2"/></svg></div>
<div class="abs hero-arrow" style="left:1129px"><svg width="14" height="14" viewBox="0 0 14 14"><path d="M5 2l5 5-5 5" fill="none" stroke="#fff" stroke-width="2"/></svg></div>

<section class="abs help"></section>
<h2 class="abs section-title" style="top:652px">HOW CAN WE <em>HELP YOU TODAY?</em></h2>

<div class="abs card blue" style="left:98px">
  <div class="icon"><svg width="34" height="34" viewBox="0 0 34 34" fill="none" stroke="#2b55a3" stroke-width="2.5"><rect x="5" y="2" width="24" height="30" rx="2"/><rect x="9" y="6" width="16" height="6"/><path d="M9 17h4M15 17h4M21 17h4M9 22h4M15 22h4M21 22h4M9 27h4M15 27h4M21 27h4"/></svg></div>
  <h3>INSURANCE</h3><hr><p>Squet bulla venenatis inser pede mi, aliquet sit amet euis auctorap stre pro tsren lreop stersce</p>
</div>
<div class="abs card green" style="left:355px">
  <div class="icon"><svg width="36" height="36" viewBox="0 0 36 36" fill="#35a57a"><path d="M3 5h12l16 16-10 10L5 15z"/><circle cx="9" cy="10" r="2.5" fill="#fff"/><path d="M19 5h3l13 13-10 10-1-1 9-9z"/></svg></div>
  <h3>MORTGAGES</h3><hr><p>Squet bulla venenatis inser pede mi, aliquet sit amet euis auctorap stre pro tsren lreop stersce</p>
</div>
<div class="abs card blue" style="left:612px">
  <div class="icon"><svg width="38" height="32" viewBox="0 0 38 32" fill="#2b55a3"><rect x="6" y="14" width="5" height="14"/><rect x="14" y="8" width="5" height="20"/><rect x="22" y="12" width="5" height="16"/><rect x="30" y="4" width="5" height="24"/><rect x="2" y="29" width="35" height="2"/><rect x="2" y="2" width="2" height="28"/></svg></div>
  <h3>BUDGETING</h3><hr><p>Squet bulla venenatis inser pede mi, aliquet sit amet euis auctorap stre pro tsren lreop stersce</p>
</div>
<div class="abs card green" style="left:867px">
  <div class="icon"><svg width="38" height="32" viewBox="0 0 38 32" fill="#35a57a"><ellipse cx="15" cy="12" rx="13" ry="9"/><path d="M6 18l-3 7 9-4z"/><ellipse cx="25" cy="19" rx="11" ry="8" stroke="#fff" stroke-width="2"/><path d="M32 24l4 6-9-3z"/></svg></div>
  <h3>BUSINESS</h3><hr><p>Squet bulla venenatis inser pede mi, aliquet sit amet euis auctorap stre pro tsren lreop stersce</p>
</div>

<h2 class="abs section-title" style="top:1118px">UPCOMMING <em>SEMINARS</em> <small>( 2 months View )</small></h2>

<div class="abs next">
  <span class="chev">‹</span>
  <div class="day">MONDAY</div>
  <div class="num">15</div>
  <div class="link">NEXT SEMINAR ⊙</div>
</div>

<div class="abs month" style="left:349px">
  <h4>FEB 2016</h4><span class="arrow">›</span>
  <div class="grid">
    <span class="h">S</span><span class="h">M</span><span class="h">T</span><span class="h">W</span><span class="h">T</span><span class="h">F</span><span class="h">S</span>
    <span class="o">28</span><span class="o">29</span><span class="o">30</span><span class="o">1</span><span class="o">2</span><span class="o">3</span><span class="o">4</span>
    <span class="o">5</span><span class="o">6</span><span class="o">7</span><span class="o c">8</span><span class="o">9</span><span class="o">10</span><span class="o">11</span>
    <span class="o">12</span><span class="o">13</span><span class="o">14</span><span class="o">15</span><span class="o">16</span><span class="o c">17</span><span class="o">18</span>
    <span class="o">19</span><span class="o">20</span><span class="o">21</span><span class="o">22</span><span class="o">23</span><span class="o">24</span><span class="o">25</span>
    <span class="o">26</span><span class="cb">27</span><span>28</span><span>29</span><span class="o">30</span><span class="o">31</span><span></span>
  </div>
  <span class="plus">+</span>
</div>
<div class="abs month" style="left:617px">
  <h4>MARCH 2016</h4><span class="arrow">›</span>
  <div class="grid">
    <span class="h">S</span><span class="h">M</span><span class="h">T</span><span class="h">W</span><span class="h">T</span><span class="h">F</span><span class="h">S</span>
    <span class="o">28</span><span class="o">29</span><span class="o">30</span><span class="o">1</span><span class="o">2</span><span class="o">3</span><span class="o">4</span>
    <span class="o">5</span><span class="o">6</span><span class="o">7</span><span class="o c">8</span><span class="o">9</span><span class="o">10</span><span class="o">11</span>
    <span class="o">12</span><span class="o">13</span><span class="o">14</span><span class="o">15</span><span class="o">16</span><span class="o c">17</span><span class="o">18</span>
    <span class="o">19</span><span class="o">20</span><span class="o">21</span><span class="o">22</span><span class="o">23</span><span class="o">24</span><span class="o">25</span>
    <span class="o">26</span><span class="cb">27</span><span>28</span><span>29</span><span class="o">30</span><span class="o">31</span><span></span>
  </div>
  <span class="plus">+</span>
</div>
<div class="abs allsem">
  <h4>VIEW ALL SEMINARS</h4>
  <ul>
    <li>Sd ut perspiciatis unde omnis isteiste natus</li>
    <li>Sd ut perspiciatis unde omnis isteiste natus</li>
    <li>Sd ut perspiciatis unde omn</li>
    <li>Sd ut perspiciatis unde omn</li>
    <li>Sd ut perspiciatis unde omnis isteiste natus</li>
  </ul>
</div>

<div class="abs events" style="top:1528px">
  <div class="event"><div class="date">30 JANUARY, 2016</div><div class="time">9.00 AM TO 11.00 AM</div><p>Sd ut perspiciatis unde omnis isteiste natus error lo sit volup ac cus antium doloremque Sd utpersp iciatis unde.</p><div class="actions"><span class="btn loc">⚲ Los Angels</span><span class="btn reg">✎ REGISTER</span></div></div>
  <div class="event"><div class="date">30 JANUARY, 2016</div><div class="time">9.00 AM TO 11.00 AM</div><p>Sd ut perspiciatis unde omnis isteiste natus error lo sit volup ac cus antium doloremque Sd utpersp iciatis unde.</p><div class="actions"><span class="btn loc">⚲ Los Angels</span><span class="btn reg">✎ REGISTER</span></div></div>
  <div class="event"><div class="date">30 JANUARY, 2016</div><div class="time">9.00 AM TO 11.00 AM</div><p>Sd ut perspiciatis unde omnis isteiste natus error lo sit volup ac cus antium doloremque Sd utpersp iciatis unde.</p><div class="actions"><span class="btn loc">⚲ Los Angels</span><span class="btn reg">✎ REGISTER</span></div></div>
  <div class="event"><div class="date">30 JANUARY, 2016</div><div class="time">9.00 AM TO 11.00 AM</div><p>Sd ut perspiciatis unde omnis isteiste natus error lo sit volup ac cus antium doloremque Sd utpersp iciatis unde.</p><div class="actions"><span class="btn loc">⚲ Los Angels</span><span class="btn reg">✎ REGISTER</span></div></div>
</div>
<div class="abs events" style="top:1796px">
  <div class="event"><div class="date">30 JANUARY, 2016</div><div class="time">9.00 AM TO 11.00 AM</div><p>Sd ut perspiciatis unde omnis isteiste natus error lo sit volup ac cus antium doloremque Sd utpersp iciatis unde.</p><div class="actions"><span class="btn loc">⚲ Los Angels</span><span class="btn reg">✎ REGISTER</span></div></div>
  <div class="event"><div class="date">30 JANUARY, 2016</div><div class="time">9.00 AM TO 11.00 AM</div><p>Sd ut perspiciatis unde omnis isteiste natus error lo sit volup ac cus antium doloremque Sd utpersp iciatis unde.</p><div class="actions"><span class="btn loc">⚲ Los Angels</span><span class="btn reg">✎ REGISTER</span></div></div>
  <div class="event"><div class="date">30 JANUARY, 2016</div><div class="time">9.00 AM TO 11.00 AM</div><p>Sd ut perspiciatis unde omnis isteiste natus error lo sit volup ac cus antium doloremque Sd utpersp iciatis unde.</p><div class="actions"><span class="btn loc">⚲ Los Angels</span><span class="btn reg">✎ REGISTER</span></div></div>
  <div class="event"><div class="date">30 JANUARY, 2016</div><div class="time">9.00 AM TO 11.00 AM</div><p>Sd ut perspiciatis unde omnis isteiste natus error lo sit volup ac cus antium doloremque Sd utpersp iciatis unde.</p><div class="actions"><span class="btn loc">⚲ Los Angels</span><span class="btn reg">✎ REGISTER</span></div></div>
</div>

<footer class="abs footer">
  <div class="abs f-brand">NORTHVALE<br>WELLNESS<br>GROUP</div>
  <div class="abs f-col" style="left:331px"><h5>Company</h5><ul><li>Home</li><li>About Us</li><li>Services</li><li>Contact</li></ul></div>
  <div class="abs f-col" style="left:498px"><h5>Links</h5><ul><li>Past experience</li><li>Services</li><li>References</li><li>Contact us</li></ul></div>
  <div class="abs f-col" style="left:696px"><h5>Support</h5><ul><li>FAQs</li><li>Privacy Policy</li><li>Recommendations</li><li>Contact</li></ul></div>
  <div class="abs f-col f-news" style="left:896px"><h5>Newsletter</h5><p>Please sign up here for latest deals</p><div class="input">Email address</div><div class="sub">SUBSCRIBE</div></div>
</footer>
<div class="abs bottom">
  <p>© 2016 Northvale Wellness Group. All right reserved &nbsp;Term of Use</p>
  <div class="social"><span></span><span></span><span></span><span></span><span></span></div>
</div>
</body>
</html>
```